Tri-Fold Brochure for Awesome School App Required!

Tulvora is a unique school app that connects teachers and parents. It is about to be launched in Australia with plans for world domination soon after :)

As part of the marketing strategy, we require a professional brochure to mail out.

We want a tri-fold brochure using the Tulvora logo colours (images attached). Front and back page should be the Tulvora blue and the inside can be white with blue borders and logo or blue with white writing although we're leaving the creativity part up to you, the experts.

As an idea, attached is an example of the content and layout required (NOTE - IT REFERS TO 'PAGES' IN THE DOCUMENT BUT I DO MEAN PANELS)
Updates

Hi All,

Thanks for taking interest in designing a brochure for Tulvora. The designs so far are great.

Note - I have attached an updated Draft design document - some of the wording has changed to make it not look so 'busy'. So please take a look at the new document.

Regards

Glen

Hi All,

Thanks for your designs so far - please keep them coming.

I have attached a 'mock screens.zip' folder - it has some images for the app. Please incorporate these into new submissions.

Regards

Glen

Hi all. Just reiterating - I would like to see some of your designs with the app screen images incorporated (in the 'mock_up.zip' folder in the attachments).

Feel free to place them anywhere you see fit - they don't just have to be on the 'app screen' page as per my original brief.

Glen

Target Market(s)

Target market is school Principals and school IT decision makers.

Industry/Entity Type

Marketing

Requirements
Must have
• - Make good use of the 6 panels of the brochure but the front panel should just be the company logo (either the elongated image across the whole panel or the vertical image in the middle - whatever looks best).
- Back panel to be logo and contact details.
- Preference is for the colour scheme to remain within the Tulvora logo colours but if you think you've got a better idea, please submit it.
**PLEASE SEE THE ATTACHED SAMPLE LAYOUT DOCUMENT**
Nice to have
• Feel free to put in non-copyrighted images relating to schools.
Feel free to invert colours, but try and stick to the Tulvora colour scheme wherever possible.

```html
<!DOCTYPE html>
<html lang="en">
<head>
<meta charset="utf-8">
<title>Tulvora Tri-Fold Brochure</title>
<link href="https://fonts.googleapis.com/css2?family=Cinzel:wght@400;600&family=EB+Garamond:wght@400;600&family=Didact+Gothic&display=swap" rel="stylesheet">
<style>
:root{
  --stage:#d6d6d8;
  --blue:#2f55bd;
  --blue-deep:#24439a;
  --black:#0b0b0c;
  --white:#ffffff;
  --sky:#7fd0f2;
  --muted:#c9d6f5;
  --photo-a:#c8ccd4;
  --photo-b:#6d7380;
}
*{box-sizing:border-box;margin:0;padding:0}
html,body{width:1200px;height:900px;overflow:hidden;background:var(--stage)}
body{font-family:"EB Garamond",Georgia,serif;color:var(--white)}
.sheet{position:absolute;left:45px;width:1110px;height:380px;display:flex;box-shadow:0 6px 18px rgba(0,0,0,.25)}
.sheet--outside{top:50px}
.sheet--inside{top:470px}
.panel{position:relative;width:370px;height:380px;overflow:hidden}
.panel--blue{background:var(--blue)}
.panel--black{background:var(--black)}
.panel + .panel{border-left:1px solid rgba(0,0,0,.18)}

/* outside */
.photo{width:100%;height:100%;background:radial-gradient(circle at 60% 40%,var(--photo-a),var(--photo-b))}
.back-mark{position:absolute;left:135px;top:120px;width:100px;height:60px;background:var(--blue);display:flex;align-items:center;justify-content:center;font-size:15px;font-weight:600;color:var(--white)}
.contact{position:absolute;left:22px;right:22px;bottom:24px;display:flex;justify-content:space-between;font-family:"Didact Gothic",Arial,sans-serif;font-size:9px;line-height:1.6;color:var(--white)}
.contact-icon{display:inline-block;width:7px;height:7px;background:var(--white);margin-right:4px;vertical-align:middle}
.cover{display:flex;flex-direction:column;align-items:center;justify-content:center;height:100%}
.cover-square{width:26px;height:26px;background:var(--sky);margin-bottom:14px}
.cover-name{font-size:58px;font-weight:400;line-height:1;color:var(--white);letter-spacing:1px}
.cover-tag{font-family:"Didact Gothic",Arial,sans-serif;font-size:11px;letter-spacing:1.5px;color:var(--sky);margin-top:8px}

/* inside */
.qmark{position:absolute;left:120px;top:-70px;font-family:"Cinzel",serif;font-size:520px;line-height:1;color:var(--black)}
.what{position:absolute;left:18px;top:60px;width:150px}
.heading{font-family:"Cinzel",serif;font-weight:400;line-height:1.05}
.heading--what{font-size:26px}
.body{font-size:8.5px;line-height:1.35;margin-top:8px}
.qa{position:absolute;left:200px;width:150px;color:var(--white)}
.qa--parents{top:30px}
.qa--schools{top:210px}
.qa-title{font-family:"Cinzel",serif;font-size:12px;line-height:1.1}
.qa ul{list-style:none;font-size:8px;line-height:1.35;margin-top:6px}
.qa li{margin-bottom:3px}

.features{padding:22px 20px}
.heading--features{font-size:34px;color:var(--blue);line-height:.95}
.heading-note{font-size:10px;color:var(--blue);font-family:"Cinzel",serif}
.modules{display:flex;gap:14px;margin-top:18px}
.module-col{flex:1}
.module{margin-bottom:14px}
.module-title{font-family:"Cinzel",serif;font-size:12px;border-bottom:1px solid var(--white);padding-bottom:3px;margin-bottom:5px}
.module p{font-size:8px;line-height:1.35;margin-bottom:3px}

.costs{padding:22px 20px}
.heading--costs{font-size:30px;text-align:center}
.fee{font-family:"Cinzel",serif;font-size:11px;text-align:center;margin-top:10px}
.fee-sub{font-size:9px;text-align:center;color:var(--muted)}
.tiers{display:flex;gap:8px;margin-top:12px}
.tier{flex:1;background:var(--blue-deep);padding:6px}
.tier-title{font-family:"Cinzel",serif;font-size:9.5px;line-height:1.1}
.tier-sub{font-size:7.5px;color:var(--muted);margin-bottom:4px}
.tier ul{list-style:none;font-size:8px;line-height:1.45}
.cost-notes{margin-top:14px;width:200px;font-family:"Cinzel",serif;font-size:8.5px;line-height:1.3}
.cost-notes p{margin-bottom:8px}
.offer{position:absolute;right:0;bottom:24px;width:120px;background:var(--black);padding:12px 10px;font-family:"Cinzel",serif;font-size:10px;line-height:1.25;text-align:center}
</style>
</head>
<body>

<section class="sheet sheet--outside" aria-label="Brochure outside">
  <div class="panel">
    <div class="photo" role="img" aria-label="Photo of a hand touching a cloud of colourful app icons"></div>
  </div>
  <div class="panel panel--black">
    <div class="back-mark">Tulvora</div>
    <div class="contact">
      <div>
        <div>Phone: 02 5550 1842</div>
        <div>Email: hello@tulvora.example</div>
      </div>
      <div>
        <div><span class="contact-icon"></span>/tulvoraschools</div>
        <div><span class="contact-icon"></span>@tulvoraapp</div>
      </div>
    </div>
  </div>
  <div class="panel panel--blue">
    <div class="cover">
      <div class="cover-square"></div>
      <div class="cover-name">tulvora</div>
      <div class="cover-tag">CONNECTING TEACHERS AND PARENTS</div>
    </div>
  </div>
</section>

<section class="sheet sheet--inside" aria-label="Brochure inside">
  <div class="panel panel--blue">
    <div class="qmark" aria-hidden="true">?</div>
    <div class="what">
      <h2 class="heading heading--what">WHAT IS TULVORA?</h2>
      <p class="body">Tulvora is an innovative mobile app that connects schools, teachers and parents like never before, giving school offices a simple way to share news with families through phones and tablets in real time, two-way communication.</p>
      <p class="body">Tulvora was designed in Canberra, for Canberra schools both large and small, and will be supported out of Canberra.</p>
    </div>
    <div class="qa qa--parents">
      <h3 class="qa-title">WHAT PROBLEMS DOES TULVORA SOLVE FOR PARENTS?</h3>
      <ul>
        <li>No more lost notes in school bags.</li>
        <li>Absences reported from a phone in seconds.</li>
        <li>Parents hear about changes as they happen.</li>
      </ul>
    </div>
    <div class="qa qa--schools">
      <h3 class="qa-title">WHAT DOES TULVORA DO FOR SCHOOLS?</h3>
      <ul>
        <li>Fewer phone calls and paper notes sent home.</li>
        <li>Less time chasing unexplained absences.</li>
        <li>A direct line to every parent at once.</li>
      </ul>
    </div>
  </div>

  <div class="panel panel--black features">
    <h2 class="heading heading--features">FEATURES OF TULVORA</h2>
    <div class="heading-note">(BROKEN INTO MODULES)</div>
    <div class="modules">
      <div class="module-col">
        <div class="module">
          <h3 class="module-title">ADMIN MODULE</h3>
          <p>Secure dashboard for school staff to manage classes.</p>
          <p>Parents and students added in minutes.</p>
          <p>Send notices to one class or the whole school.</p>
          <p>Mobile and desktop access for all staff.</p>
        </div>
      </div>
      <div class="module-col">
        <div class="module">
          <h3 class="module-title">NOTIFICATION MODULE</h3>
          <p>Push alerts for events, excursions and closures.</p>
          <p>Parents confirm they have read each notice.</p>
        </div>
        <div class="module">
          <h3 class="module-title">ABSENCE MODULE</h3>
          <p>Parents report absences with one tap.</p>
          <p>Teachers see who is away at roll call.</p>
          <p>Automatic reminders for unexplained absences.</p>
        </div>
      </div>
    </div>
  </div>

  <div class="panel panel--blue costs">
    <h2 class="heading heading--costs">TULVORA COSTS</h2>
    <div class="fee">PURCHASE FEE</div>
    <div class="fee-sub">ONCE OFF PURCHASE FEE $700</div>
    <div class="fee">ANNUAL LICENCE FEES</div>
    <div class="tiers">
      <div class="tier">
        <div class="tier-title">SINGLE MODULE</div>
        <div class="tier-sub">Any one module</div>
        <ul><li>&lt;300 students $400</li><li>&lt;600 students $600</li><li>600+ students $800</li></ul>
      </div>
      <div class="tier">
        <div class="tier-title">DOUBLE MODULE</div>
        <div class="tier-sub">Any two modules</div>
        <ul><li>&lt;300 students $700</li><li>&lt;600 students $900</li><li>600+ students $1100</li></ul>
      </div>
      <div class="tier">
        <div class="tier-title">TRIPLE MODULE</div>
        <div class="tier-sub">All three modules</div>
        <ul><li>&lt;300 students $900</li><li>&lt;600 students $1200</li><li>600+ students $1500</li></ul>
      </div>
    </div>
    <div class="cost-notes">
      <p>ALL PRICES QUOTED ARE IN AUD AND ARE EXCLUSIVE OF GST.</p>
      <p>SIGN UP FOR 3 YEARS AND RECEIVE 20% DISCOUNT ON LICENSING FEES.</p>
    </div>
    <div class="offer">FIRST 50 SCHOOLS TO SIGN UP GET THE FIRST YEAR FREE</div>
  </div>
</section>

</body>
</html>
```